Business Card Design Project

Mabel's Tonics is a natural skincare business and we need a business card designed. The company focuses on natural products and will be launching with body scrubs and bath fizzies and our mission statement is: To deliver high quality natural beauty products at a good value. It's two cards - one design - the only information changing would be name and email address

Target Market(s)

Females ages 20-50

Industry/Entity Type

Business

Requirements
Must have
• Mabel's Tonics

Corinne Halvorsen-Pitt
T: 800-417-9368
E: Corinne@MabelsTonics.example
W: www.MabelsTonics.example

Ulrich Benedetti
T: 800-417-9368
E: Ulrich@MabelsTonics.example
W: www.MabelsTonics.example
Nice to have
• I'd like to use the colors or text found at www.mabelstonics.example but I'm open to suggestions since design isn't set in stone yet. I would also like to have the words .....a little bit of magic somewhere under the company name in a different type of font. I would like a design that feels clean and maybe a retro feel to it - front and back would be nice but not mandatory

```html
<!DOCTYPE html>
<html lang="en">
<head>
<meta charset="utf-8">
<title>Mabel's Tonics – Business Card</title>
<link rel="stylesheet" href="https://fonts.googleapis.com/css2?family=Open+Sans:wght@400;600&display=swap">
<style>
  :root {
    --plum: #7d2080;
    --sky: #2c9ad6;
    --ink: #5a5a5a;
    --cream: #fbfbe6;
    --lime-wash: #eef5c4;
    --leaf: #b9d96a;
    --leaf-deep: #8fbd3a;
    --skin: #f3e1d6;
    --skin-shadow: #e6cbbd;
    --border: #d3e59a;
    --paper: #ffffff;
  }

  html, body {
    margin: 0;
    padding: 0;
    width: 1200px;
    height: 900px;
    overflow: hidden;
    background: var(--paper);
    font-family: "Open Sans", Arial, sans-serif;
  }

  .canvas {
    position: relative;
    width: 1200px;
    height: 900px;
    background: var(--paper);
  }

  .card {
    position: absolute;
    left: 0;
    top: 0;
    width: 1196px;
    height: 826px;
    border: 2px solid var(--border);
    overflow: hidden;
    background:
      radial-gradient(ellipse 70% 60% at 45% 40%, #fffff2 0%, rgba(255,255,240,0) 70%),
      linear-gradient(160deg, var(--lime-wash) 0%, var(--cream) 45%, #f6f8dc 100%);
  }

  .foliage {
    position: absolute;
    left: 0;
    top: 0;
    width: 440px;
    height: 826px;
    background:
      radial-gradient(ellipse 60% 35% at 20% 12%, rgba(185,217,106,0.75) 0%, rgba(185,217,106,0) 75%),
      radial-gradient(ellipse 45% 40% at 8% 78%, rgba(143,189,58,0.55) 0%, rgba(143,189,58,0) 75%),
      radial-gradient(ellipse 35% 30% at 40% 30%, rgba(200,225,130,0.45) 0%, rgba(200,225,130,0) 80%);
  }

  .portrait {
    position: absolute;
    right: 0;
    top: 0;
    width: 620px;
    height: 826px;
    background:
      radial-gradient(ellipse 40% 55% at 62% 48%, var(--skin) 0%, rgba(243,225,214,0.7) 45%, rgba(243,225,214,0) 80%),
      radial-gradient(ellipse 30% 20% at 40% 75%, rgba(230,203,189,0.8) 0%, rgba(230,203,189,0) 80%),
      radial-gradient(ellipse 45% 25% at 70% 6%, rgba(255,255,255,0.95) 0%, rgba(255,255,255,0) 80%);
  }

  .brand-name {
    position: absolute;
    left: 64px;
    top: 206px;
    margin: 0;
    font-size: 96px;
    font-weight: 400;
    line-height: 1;
    letter-spacing: -1px;
    color: var(--plum);
    white-space: nowrap;
  }

  .person {
    position: absolute;
    left: 70px;
    top: 430px;
    margin: 0;
    font-size: 44px;
    font-weight: 400;
    line-height: 60px;
    color: var(--plum);
    white-space: nowrap;
  }

  .person .surname-second {
    color: var(--sky);
  }

  .contacts {
    position: absolute;
    left: 70px;
    top: 484px;
    margin: 0;
    padding: 0;
    list-style: none;
    font-size: 38px;
    line-height: 58px;
    color: var(--ink);
    white-space: nowrap;
  }

  .contacts .label {
    font-weight: 600;
    color: var(--plum);
  }
</style>
</head>
<body>
<div class="canvas">
  <section class="card">
    <div class="foliage" role="img" aria-label="Soft green bamboo leaves in the upper and lower left corner"></div>
    <div class="portrait" role="img" aria-label="Photograph of a woman with a white towel on her hair holding a pink bath fizzy near her cheek"></div>

    <h1 class="brand-name">Mabel's Tonics</h1>

    <h2 class="person">Corinne Halvorsen-<span class="surname-second">Pitt</span></h2>

    <ul class="contacts">
      <li><span class="label">T</span>: 800-417-9368</li>
      <li><span class="label">E</span>: Corinne@MabelsTonics.example</li>
      <li><span class="label">W</span>: www.MabelsTonics.example</li>
    </ul>
  </section>
</div>
</body>
</html>
```